Flyer Design for Meridian Guild of Reflective Counsellors and Therapists (MGRCT)

We need a new flyer designed for MGRCT. We want to attract new members @ a tradeshow. Counsellors and Psychotherapists looking for a professional association with which to align themselves where they feel @ home because they share similar values.We would like to use the colours and leaves from our website which is www.mgrct-example.org if possible or similar colours and the photo of the tree in bloom from Facebook "stillwaterandtherapy". As well as our logo (www.mgrct-example.org), the TOVRA (www.tovra-example.org) logo as well somewhere in the bottom corner the Harmony Assembly logo (www.harmonyassembly-example.org).

Target Market(s)

Psychotherapists and Counsellors

Industry/Entity Type

Mental Health

Colors
876aae
b7a5cd
e4daeb
cadf82
abd036
9bcb3b

Requirements
Must have
• Logo
Nice to have
• Warm inviting photo of lotus flower
Should not have
• No monks

```html
<!DOCTYPE html>
<html lang="en">
<head>
<meta charset="utf-8">
<title>MGRCT Flyer</title>
<link href="https://fonts.googleapis.com/css2?family=Arimo:wght@400;700&family=Mulish:wght@600;700;800&display=swap" rel="stylesheet">
<style>
  :root {
    --purple: #876aae;
    --lavender: #b7a5cd;
    --lilac: #e4daeb;
    --lime: #cadf82;
    --green: #9bcb3b;
    --leaf: #abd036;
    --ink: #1e1e1e;
    --paper: #ffffff;
    --backdrop: #ececec;
  }
  * { box-sizing: border-box; margin: 0; padding: 0; }
  html, body { width: 869px; height: 1200px; overflow: hidden; }
  body {
    background: var(--backdrop);
    font-family: "Arimo", Arial, sans-serif;
    color: var(--ink);
    position: relative;
  }
  .page {
    position: absolute;
    left: 68px;
    width: 733px;
    background: var(--paper);
    overflow: hidden;
  }
  .page--front { top: 39px; height: 534px; }
  .page--back { top: 623px; height: 524px; }

  .diagonals { position: absolute; inset: 0; width: 100%; height: 100%; }

  .brand {
    position: absolute;
    display: flex;
    flex-direction: column;
    align-items: center;
    gap: 8px;
    font-size: 18px;
    color: #333;
    letter-spacing: .5px;
    z-index: 2;
  }
  .brand__mark {
    width: 40px; height: 40px;
    border-radius: 50%;
    background: #222;
  }
  .brand--front { left: 28px; top: 30px; }
  .brand--back { left: 620px; top: 330px; }
  .site-url {
    position: absolute; left: 16px; top: 106px;
    font-size: 12px; font-weight: 700;
  }

  .lotus-art {
    position: absolute; left: 180px; top: 30px;
    width: 145px; height: 190px;
    border-radius: 50% 50% 45% 45% / 60% 60% 40% 40%;
    background: radial-gradient(ellipse at 50% 45%, #f7b928 0%, #8dc63f 30%, #3fa9e0 55%, #d9559a 80%, rgba(217,85,154,0) 100%);
    opacity: .9;
  }
  .lotus-art--faint {
    left: 150px; top: 165px; width: 290px; height: 235px;
    opacity: .16;
    z-index: 0;
  }

  .band {
    position: absolute; left: 0; right: 0; top: 282px; bottom: 0;
    background: linear-gradient(180deg, #ece5f2 0%, var(--lilac) 100%);
  }

  .tab {
    position: absolute; left: 0;
    height: 30px;
    padding: 0 42px 0 26px;
    white-space: nowrap;
    font-family: "Mulish", sans-serif;
    font-weight: 700;
    font-size: 19px;
    line-height: 30px;
    color: #fff;
    clip-path: polygon(0 0, 100% 0, calc(100% - 22px) 100%, 0 100%);
    z-index: 2;
  }
  .tab--purple { background: var(--purple); }
  .tab--green { background: var(--green); }
  .rule {
    position: absolute; left: 0; right: 0; height: 2px;
    background: var(--purple);
    z-index: 1;
  }

  .vision-text {
    position: absolute; left: 14px; right: 20px; top: 290px;
    font-size: 9px; line-height: 12px;
    z-index: 2;
  }

  .points {
    position: absolute; left: 26px;
    list-style: none;
    font-size: 9.2px; line-height: 12px;
    z-index: 2;
  }
  .points li {
    position: relative;
    padding-left: 14px;
  }
  .points li::before {
    content: "";
    position: absolute; left: 0; top: 2px;
    width: 7px; height: 7px;
    border: 1.3px solid var(--purple);
    border-radius: 50%;
  }
  .values { top: 427px; right: 120px; }
  .values li { margin-bottom: 8px; }
  .objectives-a { top: 84px; right: 40px; }
  .objectives-a li { margin-bottom: 7.5px; }
  .objectives-b { top: 260px; right: 150px; }
  .objectives-b li { margin-bottom: 7px; }

  .footer {
    position: absolute; left: 0; right: 0; top: 410px; bottom: 0;
    background: var(--paper);
    z-index: 3;
  }
  .footer__bar {
    height: 6px;
    background: linear-gradient(90deg, var(--purple), var(--lavender));
  }
  .contact {
    position: absolute;
    font-size: 9.5px; line-height: 11px;
    font-style: normal;
  }
  .contact__name {
    font-weight: 700; color: var(--purple);
    font-size: 9.5px; margin-bottom: 8px;
  }
  .contact--head { left: 14px; top: 12px; width: 220px; }
  .contact--branch { left: 480px; top: 34px; width: 220px; }
</style>
</head>
<body>

<section class="page page--front">
  <div class="band"></div>
  <svg class="diagonals" viewBox="0 0 733 534" aria-hidden="true">
    <polygon points="480,282 733,20 733,90 560,282" fill="#d6c9e3"/>
    <polygon points="560,282 733,100 733,282" fill="#e4daeb"/>
    <polygon points="540,250 733,60 733,250" fill="#cadf82"/>
  </svg>

  <div class="brand brand--front"><span>MGRCT</span><span class="brand__mark"></span></div>
  <div class="site-url">www.mgrct-example.org</div>

  <div class="lotus-art" role="img" aria-label="Colourful lotus flower floating on rippling water"></div>

  <div class="rule" style="top:280px"></div>
  <h2 class="tab tab--purple" style="top:251px">Our Vision</h2>

  <p class="vision-text">The purpose of The Meridian Guild of Reflective Counsellors and Therapists (MGRCT), a TOVRA Member Association, is to bring the whole philosophy and practice of Buddhism (the dhamma), to therapists and counsellors, using innovative educational experiences. The benefits of introducing Buddhist practices into mental health is now scientifically validated, as increasing the effectiveness of Western psychotherapeutic approaches, as well as taking care of therapists in particular 'burnout.'<br>There is much to benefit us, as well as those we work with, in our desire to integrate Psychotherapy with Buddhism. So, MGRCT has developed and has been running a two-year professional training course in Buddhism and Psychotherapy, since 2008. The next training will begin July 2016.</p>

  <h2 class="tab tab--green" style="top:389px">Some of Our Values</h2>
  <ul class="points values">
    <li>We care about therapists</li>
    <li>We strive to be of service to our members and all those we come into contact with humility, fairness, patience and compassion</li>
    <li>We value the ongoing need for education for therapists but we also value the balance between the mind, the body and the spirit, knowing that all those need to be nourished</li>
    <li>We work in warm, generous, spirited partnership with others and we are open to working within and across sectors to influence and co-develop initiatives.</li>
  </ul>
</section>

<section class="page page--back">
  <svg class="diagonals" viewBox="0 0 733 524" aria-hidden="true">
    <polygon points="540,410 733,170 733,410" fill="#e4daeb"/>
    <polygon points="640,410 733,300 733,410" fill="#d6c9e3"/>
    <polygon points="650,170 733,80 733,170" fill="#cadf82"/>
  </svg>

  <div class="lotus-art lotus-art--faint" role="img" aria-label="Faint lotus flower in the background"></div>

  <div class="rule" style="top:63px"></div>
  <h2 class="tab tab--purple" style="top:34px">Objectives</h2>
  <ul class="points objectives-a">
    <li>To provide a philosophical base, standards and ethics for the practice of Buddhist Counselling and Psychotherapy.</li>
    <li>Maintain unique professional development of its members, as well as provide a warm and supportive community of therapists.</li>
    <li>Develop a professional organisational structure that supports the practice of Buddhist Counselling and Psychotherapy;</li>
    <li>Provide an innovative education, training and research in Buddhist Counselling and Psychotherapy;</li>
    <li>Promote Buddhist Counselling and Psychotherapy in the community;</li>
    <li>Provide accreditation practices that will support the highest quality practice in Buddhist Counselling and Psychotherapy; and</li>
    <li>Work collaboratively and beneficially with other Buddhist and Counselling and Psychotherapy Organisations.</li>
  </ul>

  <div class="rule" style="top:245px"></div>
  <h2 class="tab tab--green" style="top:216px">Objectives</h2>
  <ul class="points objectives-b">
    <li>To present Buddhism in a through way</li>
    <li>To explore and discuss dhamma and how it can improve the effectiveness of a therapist's life</li>
    <li>To provide ongoing education in all aspects of Buddhism for mental health professionals</li>
    <li>To develop a dynamic organisation that stays attuned to changes in Buddhism as it is expressed in the West</li>
    <li>To develop a strong membership/community</li>
    <li>To develop a relevant and important voice in the community</li>
    <li>To develop a unique professional identity</li>
    <li>To encourage positive social change</li>
  </ul>

  <div class="brand brand--back"><span>MGRCT</span><span class="brand__mark"></span></div>

  <footer class="footer">
    <div class="footer__bar"></div>
    <address class="contact contact--head">
      <p class="contact__name">Meridian Guild of Reflective<br>Counsellors and Therapists</p>
      <p>PO Box 4820<br>Harbourview 2999 NSW<br>Australia<br>Email: info@stillwaterandtherapy.org</p>
    </address>
    <address class="contact contact--branch">
      <p class="contact__name">Meridian Guild of Reflective<br>Counsellors and Therapists</p>
      <p>Queensland Branch<br>Email: qld@stillwaterandtherapy.org</p>
    </address>
  </footer>
</section>

</body>
</html>
```